businesscard, flyer and membercard

--------------------------------------------------------------------------------------------------
design flyer :
- delivering format (jpg, pdf and original psd)
- there is a example how the flyers should look like
the text and logo should be the same as the exemple flyer, the creativity is yours.
- the design should have a back and front side.
File format : 15,0 cm x 21,2 cm
design membercard :
- there is example how the member-card should look like
the text and logo should be the same as the exemple membercard, the creativity is yours.
- the front side contains text and open space where for writing :
Naam ......
Dansstijlen ......
- the front side contains 12 circels horizontal at the line name at the end of the line "Salsa".
- the front side contains 12 circels horizontal at the line name at the end of the line "Bachata".
- the front side contains 12 circels horizontal at the line name at the end of the line "Kizomba".
- each horizontal line with circels contains a different kind of color/design.
- file format: 7,6 cm x 10,7 cm
Business card :
- there is example how the businesscard should look like
the text and logo should be the same as the exemple buisinesscard, the creativity is yours.
- the design should have a back a front side
File format : 8,7 cm x 5,7 cm

Target Market(s)

Dancing :Salsa, Bachata and Kizomba

Colors

Designer to choose colors to be used in the design.

Requirements
Must have
• same text as seen on the examples.
Nice to have
• see the examples as attachments
Should not have
• - REMOVE TEXT "KOV" from the design
• - REMOVE TEXT "Gratis Parkeren"

```html
<!DOCTYPE html>
<html lang="nl">
<head>
<meta charset="utf-8">
<title>Nova Dance Studio – print set</title>
<link href="https://fonts.googleapis.com/css2?family=Josefin+Sans:wght@400;600;700&family=Montserrat:wght@400;500;600&display=swap" rel="stylesheet">
<style>
  :root{
    --board:#aee8fb;
    --label:#6b2d5c;
    --card-deep:#5e1a44;
    --card-mid:#8c2446;
    --card-warm:#c8383a;
    --glow:#e8743a;
    --ink:#ffffff;
    --metal:#efe2d6;
    --footer:#4a1236;
  }
  *{box-sizing:border-box;margin:0;padding:0}
  html,body{width:1200px;height:1200px;overflow:hidden}
  body{background:var(--board);position:relative;font-family:"Montserrat",sans-serif;color:var(--ink)}
  .card{position:absolute;overflow:hidden;
    background:radial-gradient(ellipse at 55% 55%,var(--card-warm) 0%,var(--card-mid) 45%,var(--card-deep) 100%);
    box-shadow:0 2px 6px rgba(60,20,50,.35)}
  .photo{position:absolute;
    background:radial-gradient(ellipse at 50% 55%,rgba(240,110,70,.85) 0%,rgba(190,50,60,.6) 45%,rgba(110,30,70,0) 75%)}
  .label{position:absolute;transform:translateX(-50%);font-family:"Montserrat",sans-serif;font-weight:600;font-size:14.5px;color:var(--label);white-space:nowrap}

  .brand{position:absolute;width:130px;text-align:center;transform:translateX(-50%)}
  .brand-name{display:inline-flex;align-items:center;gap:6px;font-family:"Josefin Sans",sans-serif;font-weight:600;font-size:22px;letter-spacing:4px;color:var(--ink)}
  .brand-dot{width:9px;height:9px;border-radius:50%;background:#e0262f}
  .brand-rule{width:110px;height:1px;background:rgba(255,255,255,.8);margin:9px auto 0}
  .brand-studio{font-family:"Montserrat",sans-serif;font-weight:600;font-size:11.5px;letter-spacing:.5px;margin-top:20px}
  .brand-tag{font-size:3px;letter-spacing:.3px;opacity:.8;margin-top:1px}
  .brand.small .brand-name{font-size:17px;letter-spacing:3px}
  .brand.small .brand-rule{width:88px;margin-top:7px}
  .brand.small .brand-studio{font-size:9px;margin-top:15px}
  .brand.small .brand-tag{font-size:2.5px}

  .styles{position:absolute;left:24px;top:140px;list-style:none}
  .styles li{display:flex;align-items:center;gap:9px;height:28px;font-family:"Josefin Sans",sans-serif;font-weight:700;font-size:20px;color:var(--metal);text-shadow:0 1px 2px rgba(0,0,0,.35)}
  .styles li::before{content:"";width:9px;height:9px;border-radius:50%;background:var(--metal);box-shadow:0 0 0 2px rgba(255,255,255,.3)}

  .contacts{position:absolute;left:24px;top:139px;list-style:none}
  .contacts li{display:flex;align-items:center;gap:9px;height:23px;font-size:10.5px;font-weight:500}
  .contacts svg{width:12px;height:12px;flex:none}

  .title{position:absolute;left:0;width:100%;text-align:center;font-family:"Josefin Sans",sans-serif;font-weight:700;color:var(--metal);text-shadow:0 1px 3px rgba(0,0,0,.4)}

  .card-footer{position:absolute;left:0;bottom:0;width:100%;height:17px;background:var(--footer);display:flex;align-items:center;justify-content:space-between;padding:0 12px;font-size:7px}
  .card-footer span{display:flex;align-items:center;gap:3px}
  .card-footer svg{width:8px;height:8px}

  .fill-in{position:absolute;left:13px;top:248px;font-family:"Montserrat",sans-serif;font-weight:500;font-size:17px;line-height:19px}
  .stamp-row{position:absolute;left:13px;width:270px;display:flex;align-items:center;justify-content:space-between}
  .stamp-row .name{font-family:"Josefin Sans",sans-serif;font-weight:700;font-size:17px;color:var(--metal)}
</style>
</head>
<body>

<!-- Business card front -->
<section class="card" style="left:209px;top:238px;width:371px;height:244px">
  <div class="photo" role="img" aria-label="Photo of a salsa dancing couple in black and red costumes" style="left:140px;top:0;width:231px;height:244px"></div>
  <div class="brand" style="left:81px;top:22px">
    <div class="brand-name">NOVA<span class="brand-dot"></span></div>
    <div class="brand-rule"></div>
    <div class="brand-studio">DANCE STUDIO</div>
    <div class="brand-tag">LET THE MUSIC MOVE US TOGETHER</div>
  </div>
  <ul class="styles">
    <li>SALSA</li><li>BACHATA</li><li>KIZOMBA</li>
  </ul>
</section>
<div class="label" style="left:380px;top:505px">BUSINESS CARD : FRONT</div>

<!-- Business card back -->
<section class="card" style="left:620px;top:238px;width:371px;height:244px">
  <div class="photo" role="img" aria-label="Photo of a salsa dancing couple in black and red costumes" style="left:140px;top:0;width:231px;height:244px"></div>
  <div class="brand" style="left:81px;top:22px">
    <div class="brand-name">NOVA<span class="brand-dot"></span></div>
    <div class="brand-rule"></div>
    <div class="brand-studio">DANCE STUDIO</div>
    <div class="brand-tag">LET THE MUSIC MOVE US TOGETHER</div>
  </div>
  <ul class="contacts">
    <li><svg viewBox="0 0 12 12"><circle cx="6" cy="4" r="2.6" fill="#fff"/><path d="M1.5 11.5c0-3 2-4.5 4.5-4.5s4.5 1.5 4.5 4.5z" fill="#fff"/></svg>Mira</li>
    <li><svg viewBox="0 0 12 12"><path d="M2.5 1l2 2.5-1 1.3c.7 1.6 1.9 2.8 3.5 3.5l1.3-1 2.5 2-1.3 1.7C5.5 10.7 1.3 6.5.8 2.3z" fill="none" stroke="#fff" stroke-width="1"/></svg>0612 345 678</li>
    <li><svg viewBox="0 0 12 12"><rect x="1" y="3" width="10" height="7" fill="none" stroke="#fff" stroke-width="1"/><path d="M1 3l5 4 5-4" fill="none" stroke="#fff" stroke-width="1"/></svg>novadenhaag@mail.nl</li>
    <li><svg viewBox="0 0 12 12"><rect x="1" y="1" width="10" height="10" rx="2" fill="#fff"/></svg>novadenhaag</li>
  </ul>
</section>
<div class="label" style="left:813px;top:505px">BUSINESS CARD : BACK</div>

<!-- Member card back -->
<section class="card" style="left:286px;top:606px;width:294px;height:413px">
  <div class="photo" role="img" aria-label="Photo of a salsa dancing couple with palm trees behind" style="left:0;top:30px;width:294px;height:300px"></div>
  <div class="brand small" style="left:231px;top:26px">
    <div class="brand-name">NOVA<span class="brand-dot"></span></div>
    <div class="brand-rule"></div>
    <div class="brand-studio">DANCE STUDIO</div>
    <div class="brand-tag">LET THE MUSIC MOVE US TOGETHER</div>
  </div>
  <div class="title" style="top:310px;font-size:29px">SALSA-BACHATA</div>
  <div class="title" style="top:346px;font-size:29px">&amp; KIZOMBA</div>
  <footer class="card-footer">
    <span><svg viewBox="0 0 12 12"><rect x="1" y="3" width="10" height="7" fill="none" stroke="#fff" stroke-width="1.4"/><path d="M1 3l5 4 5-4" fill="none" stroke="#fff" stroke-width="1.4"/></svg>novadenhaag@mail.nl</span>
    <span><svg viewBox="0 0 12 12"><rect x="1" y="1" width="10" height="10" rx="2" fill="#fff"/></svg>novadenhaag</span>
    <span><svg viewBox="0 0 12 12"><path d="M2.5 1l2 2.5-1 1.3c.7 1.6 1.9 2.8 3.5 3.5l1.3-1 2.5 2-1.3 1.7C5.5 10.7 1.3 6.5.8 2.3z" fill="none" stroke="#fff" stroke-width="1.2"/></svg>0612 345 678</span>
  </footer>
</section>
<div class="label" style="left:430px;top:1046px">MEMBERCARD :</div>

<!-- Member card front -->
<section class="card" style="left:620px;top:606px;width:294px;height:413px">
  <div class="photo" role="img" aria-label="Photo of a salsa dancing couple with palm trees behind" style="left:0;top:30px;width:294px;height:300px"></div>
  <div class="brand small" style="left:231px;top:26px">
    <div class="brand-name">NOVA<span class="brand-dot"></span></div>
    <div class="brand-rule"></div>
    <div class="brand-studio">DANCE STUDIO</div>
    <div class="brand-tag">LET THE MUSIC MOVE US TOGETHER</div>
  </div>
  <div class="fill-in">Naam ...................<br>Dansstijlen ...................</div>

  <div class="stamp-row" style="top:303px">
    <span class="name">SALSA</span>
    <svg width="182" height="14" viewBox="0 0 182 14">
      <g fill="#fff" stroke-width="2">
        <circle cx="7" cy="7" r="5.5" stroke="#e0262f"/><circle cx="22.3" cy="7" r="5.5" stroke="#2a52d8"/>
        <circle cx="37.6" cy="7" r="5.5" stroke="#f3d22b" fill="#fff7b0"/><circle cx="52.9" cy="7" r="5.5" stroke="#3bbb3b"/>
        <circle cx="68.2" cy="7" r="5.5" stroke="#e0262f"/><circle cx="83.5" cy="7" r="5.5" stroke="#2a52d8"/>
        <circle cx="98.8" cy="7" r="5.5" stroke="#f3d22b" fill="#fff7b0"/><circle cx="114.1" cy="7" r="5.5" stroke="#3bbb3b"/>
        <circle cx="129.4" cy="7" r="5.5" stroke="#e0262f"/><circle cx="144.7" cy="7" r="5.5" stroke="#2a52d8"/>
        <circle cx="160" cy="7" r="5.5" stroke="#f3d22b" fill="#fff7b0"/><circle cx="175.3" cy="7" r="5.5" stroke="#3bbb3b"/>
      </g>
    </svg>
  </div>
  <div class="stamp-row" style="top:334px">
    <span class="name">BACHATA</span>
    <svg width="182" height="14" viewBox="0 0 182 14">
      <g stroke-width="2">
        <circle cx="7" cy="7" r="5.5" stroke="#e0262f" fill="#fff"/><circle cx="22.3" cy="7" r="5.5" stroke="#2a52d8" fill="#dde6ff"/>
        <circle cx="37.6" cy="7" r="5.5" stroke="#f3d22b" fill="#fff7b0"/><circle cx="52.9" cy="7" r="5.5" stroke="#3bbb3b" fill="#fff"/>
        <circle cx="68.2" cy="7" r="5.5" stroke="#e0262f" fill="#fff"/><circle cx="83.5" cy="7" r="5.5" stroke="#2a52d8" fill="#dde6ff"/>
        <circle cx="98.8" cy="7" r="5.5" stroke="#f3d22b" fill="#fff7b0"/><circle cx="114.1" cy="7" r="5.5" stroke="#3bbb3b" fill="#fff"/>
        <circle cx="129.4" cy="7" r="5.5" stroke="#e0262f" fill="#fff"/><circle cx="144.7" cy="7" r="5.5" stroke="#2a52d8" fill="#dde6ff"/>
        <circle cx="160" cy="7" r="5.5" stroke="#f3d22b" fill="#fff7b0"/><circle cx="175.3" cy="7" r="5.5" stroke="#3bbb3b" fill="#fff"/>
      </g>
    </svg>
  </div>
  <div class="stamp-row" style="top:365px">
    <span class="name">KIZOMBA</span>
    <svg width="182" height="14" viewBox="0 0 182 14">
      <g stroke-width="2">
        <circle cx="7" cy="7" r="5.5" stroke="#e0262f" fill="#fff"/><circle cx="22.3" cy="7" r="5.5" stroke="#2a52d8" fill="#fff"/>
        <circle cx="37.6" cy="7" r="5.5" stroke="#f3d22b" fill="#fff36a"/><circle cx="52.9" cy="7" r="5.5" stroke="#3bbb3b" fill="#fff"/>
        <circle cx="68.2" cy="7" r="5.5" stroke="#e0262f" fill="#fff"/><circle cx="83.5" cy="7" r="5.5" stroke="#2a52d8" fill="#fff"/>
        <circle cx="98.8" cy="7" r="5.5" stroke="#f3d22b" fill="#fff36a"/><circle cx="114.1" cy="7" r="5.5" stroke="#3bbb3b" fill="#fff"/>
        <circle cx="129.4" cy="7" r="5.5" stroke="#e0262f" fill="#fff"/><circle cx="144.7" cy="7" r="5.5" stroke="#2a52d8" fill="#fff"/>
        <circle cx="160" cy="7" r="5.5" stroke="#f3d22b" fill="#fff36a"/><circle cx="175.3" cy="7" r="5.5" stroke="#3bbb3b" fill="#fff"/>
      </g>
    </svg>
  </div>
  <footer class="card-footer">
    <span><svg viewBox="0 0 12 12"><path d="M1 6.5L6 2l5 4.5H9.5V11h-2V8h-3v3h-2V6.5z" fill="#fff"/></svg>Parklaan 22, 2514 AB Den Haag</span>
    <span><svg viewBox="0 0 12 12"><rect x="1" y="1" width="10" height="10" rx="2" fill="#fff"/></svg>novadenhaag</span>
    <span><svg viewBox="0 0 12 12"><path d="M2.5 1l2 2.5-1 1.3c.7 1.6 1.9 2.8 3.5 3.5l1.3-1 2.5 2-1.3 1.7C5.5 10.7 1.3 6.5.8 2.3z" fill="none" stroke="#fff" stroke-width="1.2"/></svg>0612 345 678</span>
  </footer>
</section>
<div class="label" style="left:773px;top:1046px">MEMBERCARD :</div>

</body>
</html>
```